Lorabelle Hair Flyer - tri-fold

I have added 2 participation payments to the project. I am not sure how I allocate them, but I would like to award them to two particular designers. When I find out how to do it I will allocate them. Thank you to everyone that participated, most designs were outstanding, and it was very hard to chose a winner.
========================================
PLEASE NO NEW DESIGNERS. I HAVE ENOUGH GOOD DESIGNS NOW, THAT I WILL WORK WITH ON THE EXISTING DESIGNERS. THANK YOU FOR ALL PARTICIPATING. THE QUALITY OF ALL SUBMISSIONS HAS EXCEEDED MY EXPECTATIONS, AND IS MAKING THE CHOICE DIFFICULT.
==============================================================

I have attached a proof pdf which is my draft design (I just used a stock template from Printorra) to do the mock up.

I would like you to replace the 3 main pictures of models with those I have attached. The name of the files will tell you where they should go.
I have attached pictures of all the stock photos as well, and most of the text is in the text file to save you typing it in.

I want the background colour to match Lorabelle colours so black with a fade to gold or something like that, must look sophisticated. I have attached Lorabelle logo files in black and white background.

The main pictures I have attached from the models will need to be blended into the background as well, but the hair still needs to be visible (might be hard given it is black hair as well,). The title stripes should be a gold fade as well, and the lorabelle text should be replaced with our logo.

please also add in the plain square mark and ChatLine logo's in the appropriate places. The dimensions should be 279mm * 216mm and print in the PrintOrra tri-fold brochure.

Possible ongoing work for the winning person, as the original designer of the logo only does logos/business cards, not other print material. Have logos in other formats (ai/cdr/jpeg) if required

Target Market(s)

African women

Industry/Entity Type

Hair

Font styles to use
Serif

Requirements
Must have
• Logo, product pictures, attached text, layout changes to draft mock up is ok if it looks better. Must conform to Printorra tri-fold layout
Nice to have
• Based on logo colours, black, white, gold complimentary colours to that palette are ok

```html
<!DOCTYPE html>
<html lang="en">
<head>
<meta charset="utf-8">
<title>Lorabelle Hair – Tri-fold Inside</title>
<link rel="stylesheet" href="https://fonts.googleapis.com/css2?family=Didact+Gothic&family=Cinzel:wght@500&family=Arimo&display=swap">
<style>
  :root{
    --stage:#e4e4e4;
    --gold:#c9a227;
    --gold-light:#e8c65a;
    --gold-deep:#8a6a12;
    --black:#0b0b0b;
    --ink:#161616;
    --white:#ffffff;
    --muted:#e9dcae;
  }
  *{margin:0;padding:0;box-sizing:border-box}
  html,body{width:1200px;height:1000px;overflow:hidden}
  body{background:var(--stage);position:relative;font-family:"Didact Gothic",sans-serif}

  .brochure{
    position:absolute;left:60px;top:35px;width:1082px;height:852px;overflow:hidden;
    background:linear-gradient(180deg,var(--gold) 0%,#a88419 22%,#4a3a0c 50%,#141414 72%,var(--black) 100%);
    box-shadow:4px 6px 10px rgba(0,0,0,.35);
  }
  .decor{position:absolute;left:0;top:0}

  .model-photo{
    position:absolute;left:590px;top:125px;width:492px;height:727px;
    background:
      radial-gradient(ellipse 30% 22% at 62% 38%,#c99a7c 0%,rgba(201,154,124,.6) 55%,transparent 100%),
      radial-gradient(ellipse 70% 80% at 60% 55%,#1a1a1a 0%,#0e0e0e 70%,transparent 100%);
  }

  .section-bar{
    position:absolute;background:var(--black);color:var(--white);font-size:19px;
    display:flex;align-items:center;
  }
  .products-bar{left:2px;top:25px;width:324px;height:34px;justify-content:flex-end;padding-right:14px}
  .ranges-bar{left:462px;top:364px;width:158px;height:27px;justify-content:center;font-size:18px}

  .products-intro{position:absolute;left:40px;top:67px;font-size:12.5px;color:var(--muted)}

  .product{position:absolute;width:132px;text-align:center}
  .product .frame{
    width:132px;height:132px;border:4px solid #b99a45;background:var(--white);
    display:flex;align-items:center;justify-content:center;
  }
  .product .swatch{width:104px;height:96px;background:radial-gradient(ellipse at 50% 50%,#2a2a2a 0%,#111 60%,#3a3a3a 100%);border-radius:6px}
  .product .label{display:block;margin-top:9px;font-size:13px;color:var(--white)}

  .frontal-note{
    position:absolute;left:402px;top:302px;width:274px;height:32px;border:1px solid #d8c27a;border-radius:5px;
    color:var(--gold-light);font-size:17.5px;display:flex;align-items:center;justify-content:center;
  }

  .ranges-copy{position:absolute;left:413px;top:404px;width:250px;color:#e6e6e6;font-size:12.2px;line-height:17px}
  .ranges-copy p+p{margin-top:17px}

  .phone{position:absolute;left:445px;top:622px;display:flex;align-items:center;gap:8px;color:var(--white);font-family:"Arimo",sans-serif;font-size:20px}

  .brand{position:absolute;left:70px;top:660px;width:220px;text-align:center;color:var(--white)}
  .brand-dot{position:absolute;left:233px;top:663px;width:56px;height:56px;border-radius:50%;background:var(--white)}
  .brand-name{position:absolute;left:60px;top:748px;width:240px;text-align:center;font-family:"Cinzel",serif;font-weight:500;font-size:33px;color:var(--white);letter-spacing:1px}
  .brand-tag{position:absolute;left:60px;top:786px;width:240px;text-align:center;font-family:"Arimo",sans-serif;font-size:13px;color:var(--white)}
  .brand-rule{position:absolute;left:77px;top:814px;width:205px;height:2px;background:linear-gradient(90deg,transparent,var(--gold),transparent)}

  .contact-lines{position:absolute;left:462px;top:780px;color:var(--white);font-size:10.5px;line-height:16px}
  .contact-lines span.mark{display:inline-block;width:10px;height:10px;vertical-align:-1px;margin:0 2px 0 3px;background:var(--gold)}
  .contact-lines span.round{border-radius:50%}

  .caption{position:absolute;left:0;top:910px;width:1200px;text-align:center;font-family:"Arimo",sans-serif;font-size:36px;color:#222}
</style>
</head>
<body>
  <main class="brochure">
    <svg class="decor" width="1082" height="852" viewBox="0 0 1082 852" aria-hidden="true">
      <defs>
        <linearGradient id="swoosh" x1="0" y1="0" x2="1" y2="1">
          <stop offset="0" stop-color="#b58a14"/>
          <stop offset=".5" stop-color="#f0cf62"/>
          <stop offset="1" stop-color="#b8901e"/>
        </linearGradient>
      </defs>
      <path d="M650,0 C720,90 880,150 1082,150 L1082,128 C890,126 760,70 705,0 Z" fill="url(#swoosh)"/>
      <path d="M0,660 C140,600 330,585 480,650 C600,705 690,780 770,800 L770,852 L0,852 Z" fill="#101010"/>
      <path d="M0,660 C140,600 330,585 480,650 C600,705 690,780 770,800" fill="none" stroke="url(#swoosh)" stroke-width="9"/>
    </svg>

    <div class="model-photo" role="img" aria-label="Model with long wavy black hair, blended into the dark background"></div>

    <div class="section-bar products-bar">Our Products</div>
    <p class="products-intro">We provide Natural 100g Wefts in the following styles</p>

    <div class="product" style="left:39px;top:96px"><div class="frame"><div class="swatch" role="img" aria-label="Straight hair weft"></div></div><span class="label">Straight</span></div>
    <div class="product" style="left:193px;top:96px"><div class="frame"><div class="swatch" role="img" aria-label="Body wave hair bundles"></div></div><span class="label">Body Wave</span></div>
    <div class="product" style="left:398px;top:100px"><div class="frame"><div class="swatch" role="img" aria-label="Lace closure piece"></div></div><span class="label">Jerry Curl</span></div>
    <div class="product" style="left:552px;top:100px"><div class="frame"><div class="swatch" role="img" aria-label="Curly hair bundles"></div></div><span class="label">Matching Closures</span></div>
    <div class="product" style="left:39px;top:264px"><div class="frame"><div class="swatch" role="img" aria-label="Deep wave hair bundles"></div></div><span class="label">Deep Wave</span></div>
    <div class="product" style="left:193px;top:264px"><div class="frame"><div class="swatch" role="img" aria-label="Fumi curl hair bundles"></div></div><span class="label">Fumi Curl</span></div>
    <div class="product" style="left:39px;top:437px"><div class="frame"><div class="swatch" role="img" aria-label="Romance curl hair bundles"></div></div><span class="label">Romance Curl</span></div>
    <div class="product" style="left:193px;top:437px"><div class="frame"><div class="swatch" role="img" aria-label="Kinky curl hair bundles"></div></div><span class="label">Kinky Curl</span></div>

    <div class="frontal-note">We Also Sell 360 Frontal Closures</div>

    <div class="section-bar ranges-bar">Ranges</div>
    <div class="ranges-copy">
      <p>We have two ranges to give our customers choice, our Platinum range is sourced from India and comes from a single donor.</p>
      <p>Our Premium range is sourced from donors from Asia and are typically referred to as Brazilian or Peruvian in the Industry.</p>
      <p>Both are 100% Virgin Remy hair. Both come with a 1 year Warranty, both are the highest quality hair in the industry</p>
    </div>

    <div class="phone">
      <svg width="18" height="18" viewBox="0 0 18 18" aria-hidden="true">
        <circle cx="9" cy="9" r="8" fill="none" stroke="#c9a227" stroke-width="1.6"/>
        <path d="M6,5 L7.5,5 L8.2,7 L7.2,7.8 C7.7,9 8.7,10 10,10.6 L10.8,9.6 L12.8,10.3 L12.8,11.8 C9,12.2 5.8,9 6,5 Z" fill="#c9a227"/>
      </svg>
      +61 400 555 019
    </div>

    <div class="brand-dot"></div>
    <div class="brand-name">LORABELLE</div>
    <div class="brand-tag">100% Human Hair</div>
    <div class="brand-rule"></div>

    <div class="contact-lines">
      Or contact either on<span class="mark round"></span>ChatLine<br>
      Follow us on<span class="mark"></span>Lorabellehairng
    </div>
  </main>
  <div class="caption">Inside</div>
</body>
</html>
```